Business Card Design for a Private Label Pet Company

We need a business card design for our family-owned company, Harbor Paw Works (www.harborpawworks-example.com), out of St. Louis, MO. We provide turnkey private label solutions for retailers, Cartwell sellers and other brands who want to provide high quality, natural, Made in the USA pet products to their customers. Our customer are worldwide and range from the US to the UK to Vietnam and beyond. We offer private label for dozens of pet products including grooming products (shampoos, conditioners, colognes, ear and eye washes, mouthwash, etc.), all meat treats, supplements, and specialty products (pet stain and odor cleaner, anti-chew spray, etc.). We would like to see designs that use the colors, fonts and logos (see variations) within our brand guidelines and fit with the look and feel from our website.

Target Market(s)

Pet Store Owners, Cartwell Sellers, Pet Brand Marketers

Industry/Entity Type

Pet

Contact Information for Business Card

Lyle Dorsett
CEO
Harbor Paw Works
5817 Wexmoor Commerce Lane
St. Louis, MO 63188
office: 314.555.0182
mobile: 770.555.0139
email: lyle@harborpawworks-example.com

Colors

Designer to choose colors to be used in the design.

Requirements
Must have
• Need to follow the brand guidelines attached for colors, fonts and logos
• Need to use the logos attached (or a variation) with our without the tagline
• Name, title, phone (office and mobil), email, address on the business card
• Clean professional look and feel that says: high quality natural pet products, high quality service, made in the USA
Nice to have
• Made in the USA is a big positive in our industry and we are very proud of it. There is an attached icon from our website. The designer can get creative here as they wish.
• I do like using color for pop. Just don't like lots of bright, loud colors.
Should not have
• lots of bright, loud colors
• overwhelming to the reader
• crowded

```html
<!DOCTYPE html>
<html lang="en">
<head>
<meta charset="utf-8">
<title>Harbor Paw Works – Business Card</title>
<link rel="stylesheet" href="https://fonts.googleapis.com/css2?family=Oswald:wght@700&family=Crimson+Pro:wght@400;500&family=Montserrat:wght@500&display=swap">
<style>
  :root {
    --forest: #3b504d;
    --olive: #5d6a2e;
    --paper: #ffffff;
    --backdrop: #e7e4df;
    --photo-grass: #5f8f32;
    --photo-fur: #b8733a;
    --photo-light: #e9ddcf;
    --badge-ring: #cbbfa9;
    --ink-light: #f3f3f0;
  }
  * { box-sizing: border-box; margin: 0; padding: 0; }
  html, body { width: 1200px; height: 1200px; overflow: hidden; }
  body {
    background: var(--backdrop);
    position: relative;
    font-family: "Crimson Pro", Georgia, serif;
  }
  .card {
    position: absolute;
    left: 150px;
    width: 900px;
    height: 514px;
    background: var(--paper);
    overflow: hidden;
    box-shadow: 0 6px 18px rgba(0,0,0,.18);
  }
  .card--front { top: 52px; }
  .card--back { top: 630px; }

  /* Front */
  .front-photo {
    position: absolute; inset: 0;
    width: 900px; height: 514px;
  }
  .made-badge {
    position: absolute; left: 70px; top: 290px;
    width: 190px; height: 190px;
  }
  .wordmark {
    font-family: "Oswald", "Arial Narrow", sans-serif;
    font-weight: 700;
    color: var(--forest);
    text-transform: uppercase;
    line-height: 1;
    letter-spacing: 1px;
    white-space: nowrap;
  }
  .front-wordmark {
    position: absolute; right: 50px; top: 316px;
    font-size: 52px;
  }
  .web-pill {
    position: absolute; left: 420px; top: 402px;
    width: 480px; height: 50px;
    background: var(--forest);
    border-radius: 25px 0 0 25px;
    color: var(--ink-light);
    font-size: 24px;
    white-space: nowrap;
    display: flex; align-items: center;
    padding-left: 36px;
  }

  /* Back */
  .back-brand {
    position: absolute; left: 0; top: 0;
    width: 520px; height: 514px;
    display: flex; align-items: center; justify-content: center;
  }
  .back-wordmark { font-size: 48px; }
  .contact-panel {
    position: absolute; right: 0; top: 0;
    width: 380px; height: 514px;
    background: var(--forest);
    color: var(--ink-light);
    padding: 60px 24px 0 36px;
  }
  .person-name { font-size: 38px; font-weight: 400; line-height: 1; }
  .person-title { font-size: 20px; margin: 4px 0 28px 110px; }
  .contact-row {
    display: grid; grid-template-columns: 26px 1fr;
    column-gap: 10px; align-items: start;
    font-size: 18px; line-height: 1.3;
    margin-bottom: 10px;
    white-space: nowrap;
  }
  .contact-row svg { margin-top: 4px; }
  .panel-brand {
    margin-top: 26px;
    text-align: center;
    border-bottom: 1px solid rgba(255,255,255,.5);
    padding-bottom: 6px;
  }
  .panel-wordmark { color: var(--ink-light); font-size: 30px; }
  .tagline {
    font-family: "Montserrat", Arial, sans-serif;
    font-size: 11px; letter-spacing: 1px;
    text-align: center; margin-top: 6px;
  }
</style>
</head>
<body>

<section class="card card--front" aria-label="Card front">
  <svg class="front-photo" viewBox="0 0 900 514" role="img" aria-label="Photo of a golden dog and an orange and white cat resting together on green grass">
    <defs>
      <linearGradient id="photoTone" x1="0" y1="0" x2="1" y2="0">
        <stop offset="0" stop-color="var(--photo-fur)"/>
        <stop offset=".45" stop-color="var(--photo-grass)"/>
        <stop offset=".75" stop-color="var(--photo-light)"/>
        <stop offset="1" stop-color="var(--photo-grass)"/>
      </linearGradient>
    </defs>
    <polygon points="0,0 900,0 900,120 0,330" fill="url(#photoTone)"/>
  </svg>

  <svg class="made-badge" viewBox="0 0 190 190" role="img" aria-label="Made in the USA seal">
    <circle cx="95" cy="95" r="92" fill="#fff" stroke="var(--badge-ring)" stroke-width="3"/>
    <circle cx="95" cy="95" r="66" fill="#b8333a"/>
  </svg>

  <div class="wordmark front-wordmark">Harbor Paw Works</div>
  <div class="web-pill">www.harborpawworks-example.com</div>
</section>

<section class="card card--back" aria-label="Card back">
  <div class="back-brand">
    <div class="wordmark back-wordmark">Harbor Paw Works</div>
  </div>

  <div class="contact-panel">
    <h1 class="person-name">Lyle Dorsett</h1>
    <p class="person-title">CEO</p>

    <div class="contact-row">
      <svg width="18" height="22" viewBox="0 0 18 22" aria-hidden="true"><path d="M9 1a7 7 0 0 0-7 7c0 5 7 13 7 13s7-8 7-13a7 7 0 0 0-7-7z" fill="#fff"/><circle cx="9" cy="8" r="2.6" fill="var(--forest)"/></svg>
      <div>Harbor Paw Works<br>5817 Wexmoor Commerce Lane<br>St. Louis, MO 63188<br>Office: 314.555.0182</div>
    </div>
    <div class="contact-row">
      <svg width="20" height="20" viewBox="0 0 20 20" aria-hidden="true"><circle cx="10" cy="6" r="4" fill="#fff"/><path d="M2 19c0-5 4-7 8-7s8 2 8 7z" fill="#fff"/></svg>
      <div>mobile: 770.555.0139<br>lyle@harborpawworks-example.com</div>
    </div>
    <div class="contact-row">
      <svg width="18" height="18" viewBox="0 0 18 18" aria-hidden="true" fill="none" stroke="#fff" stroke-width="1.4"><circle cx="9" cy="9" r="7.5"/><ellipse cx="9" cy="9" rx="3.5" ry="7.5"/><path d="M1.5 9h15M3 5h12M3 13h12"/></svg>
      <div>harborpawworks-example.com</div>
    </div>

    <div class="panel-brand">
      <div class="wordmark panel-wordmark">Harbor Paw Works</div>
    </div>
    <p class="tagline">TURNKEY PRIVATE LABEL PARTNER</p>
  </div>
</section>

</body>
</html>
```